Test and Tag business card design

We are an appliance test and tag company in Brisbane Australia requiring a business card design.
I don't have a logo.
Card front: Matte black background with white font.
Card back: White background with black font colour
Examples are attached
Minimalist design
Reason: Looking for more designs with an extreme minimal feel
Industry/Entity Type
Appliance
Contact Information for Business Card
Business name: Summit Check and Label
Description: Onsite Electrical Testing and Tagging
Licence No. 48213
Name: Greg Palmby
Mobile: 0417 592 348
Email: greg@summitcheckandlabel.com.au
Web: summitcheckandlabel.com.au
Logo Text
Summit Check and Label
Look and feel

```html
<!DOCTYPE html>
<html lang="en">
<head>
<meta charset="utf-8">
<title>Summit Check and Label – Business Card</title>
<link rel="stylesheet" href="https://fonts.googleapis.com/css2?family=Questrial&display=swap">
<style>
  :root {
    --stage: #1e1e1f;
    --card-black: #232325;
    --card-white: #ecebe8;
    --ink-white: #e6e6e6;
    --ink-muted: #b9b9bb;
    --ink-black: #1f1f20;
    --divider: #5a5a5c;
  }
  * { box-sizing: border-box; margin: 0; padding: 0; }
  html, body {
    width: 1200px; height: 900px; overflow: hidden;
    background: var(--stage);
    font-family: "Questrial", "Century Gothic", sans-serif;
  }
  .canvas {
    width: 1200px; height: 900px;
    display: flex; flex-direction: column;
    align-items: center; justify-content: center; gap: 40px;
  }
  .card {
    width: 640px; height: 391px; position: relative;
    border-radius: 3px;
    box-shadow: 0 10px 30px rgba(0,0,0,.45);
  }
  /* back */
  .card-back { background: var(--card-white); color: var(--ink-black); }
  .card-back .business-name {
    position: absolute; top: 152px; left: 0; right: 0;
    text-align: center; font-size: 24px; letter-spacing: .3px;
  }
  .card-back .web {
    position: absolute; bottom: 40px; left: 0; right: 0;
    text-align: center; font-size: 14px; letter-spacing: .6px;
  }
  /* front */
  .card-front { background: var(--card-black); color: var(--ink-white); }
  .card-front .business-name {
    position: absolute; top: 162px; left: 40px; width: 262px;
    font-size: 21px; letter-spacing: .3px; white-space: nowrap;
  }
  .card-front .divider {
    position: absolute; left: 322px; top: 110px;
    width: 1px; height: 130px; background: var(--divider);
  }
  .contact { position: absolute; left: 350px; top: 112px; }
  .contact .name {
    font-size: 17px; letter-spacing: 1px; text-transform: uppercase; margin-bottom: 14px;
  }
  .contact ul { list-style: none; }
  .contact li {
    display: flex; align-items: center; gap: 10px;
    font-size: 13px; color: var(--ink-muted); margin-bottom: 8px;
  }
  .contact svg { width: 14px; height: 14px; flex: none; }
  .card-front .tagline {
    position: absolute; bottom: 44px; left: 0; right: 0;
    text-align: center; font-size: 15px; letter-spacing: .5px; color: var(--ink-muted);
  }
</style>
</head>
<body>
<main class="canvas">
  <section class="card card-back" aria-label="Card back">
    <p class="business-name">Summit Check and Label</p>
    <p class="web">www.summitcheckandlabel.com.au</p>
  </section>

  <section class="card card-front" aria-label="Card front">
    <p class="business-name">Summit Check and Label</p>
    <div class="divider"></div>
    <div class="contact">
      <p class="name">Greg Palmby</p>
      <ul>
        <li>
          <svg viewBox="0 0 14 14" aria-hidden="true"><circle cx="7" cy="7" r="7" fill="#e6e6e6"/><path d="M4.5 3.8l1.4-.3.8 1.9-.9.7a5 5 0 0 0 2.1 2.1l.7-.9 1.9.8-.3 1.4c-3.2.2-5.9-2.5-5.7-5.7z" fill="#232325"/></svg>
          0417 592 348
        </li>
        <li>
          <svg viewBox="0 0 14 14" aria-hidden="true"><circle cx="7" cy="7" r="7" fill="#e6e6e6"/><rect x="3.5" y="4.5" width="7" height="5" fill="none" stroke="#232325" stroke-width="1"/><path d="M3.5 4.5L7 7.3l3.5-2.8" fill="none" stroke="#232325" stroke-width="1"/></svg>
          greg@summitcheckandlabel.com.au
        </li>
        <li>
          <svg viewBox="0 0 14 14" aria-hidden="true"><circle cx="7" cy="7" r="7" fill="#e6e6e6"/><circle cx="7" cy="7" r="3.8" fill="none" stroke="#232325" stroke-width=".9"/><path d="M3.2 7h7.6M7 3.2c-1.6 2.2-1.6 5.4 0 7.6M7 3.2c1.6 2.2 1.6 5.4 0 7.6" fill="none" stroke="#232325" stroke-width=".8"/></svg>
          www.summitcheckandlabel.com.au
        </li>
      </ul>
    </div>
    <p class="tagline">Onsite Electrical Testing and Tagging Licence No. 48213</p>
  </section>
</main>
</body>
</html>
```